KVRo Business Cards

We need a business card design. We are a Technology (Audio Visual) design, sales and installation company. Looking for a double sided design, clean

Contact Information for Business Card

Clean, modern look, 2 sided

Font styles to use
Sans Serif

```html
<!DOCTYPE html>
<html lang="en">
<head>
<meta charset="utf-8">
<title>KVRo Business Cards</title>
<link rel="stylesheet" href="https://fonts.googleapis.com/css2?family=Montserrat:wght@400;500;700&display=swap">
<style>
  :root {
    --backdrop: #e4e4e2;
    --card: #2b2b2b;
    --card-shade: #262626;
    --accent: #f7941d;
    --ink-light: #ffffff;
    --ink-muted: #d6d6d6;
    --rule: #6b6b6b;
  }
  * { box-sizing: border-box; margin: 0; padding: 0; }
  html, body {
    width: 1200px; height: 801px; overflow: hidden;
    background: var(--backdrop);
    font-family: "Montserrat", sans-serif;
  }
  .canvas {
    position: relative; width: 1200px; height: 801px;
    display: flex; align-items: center; justify-content: center; gap: 48px;
  }
  .card {
    position: relative; width: 525px; height: 300px;
    background: var(--card);
    border-bottom: 4px solid var(--accent);
    border-left: 2px solid var(--accent);
    box-shadow: 0 10px 24px rgba(0,0,0,0.22);
    overflow: hidden;
  }
  .wordmark {
    font-weight: 700; color: var(--ink-light);
    letter-spacing: 1px; line-height: 1;
  }
  /* front side */
  .card-front .wordmark {
    position: absolute; left: 48px; top: 124px; font-size: 54px;
  }
  .card-front .divider {
    position: absolute; left: 255px; top: 60px;
    width: 1px; height: 180px; background: var(--rule);
  }
  .contact {
    position: absolute; left: 282px; top: 70px;
    color: var(--ink-muted); font-size: 12.5px; line-height: 1.45;
  }
  .contact .name {
    color: var(--accent); font-weight: 500; font-size: 16px;
    letter-spacing: 0.5px; text-transform: uppercase; line-height: 1.2;
  }
  .contact .role { font-size: 14px; margin-bottom: 8px; }
  .contact .address { margin-bottom: 8px; }
  .contact-line { display: flex; align-items: center; gap: 8px; }
  .contact-line svg { width: 11px; height: 11px; flex: none; }
  .contact .web-accent { color: var(--accent); }
  /* back side */
  .card-back {
    background: linear-gradient(160deg, var(--card) 0%, var(--card-shade) 100%);
  }
  .card-back .wordmark {
    position: absolute; right: 44px; bottom: 64px; font-size: 70px;
  }
</style>
</head>
<body>
<main class="canvas">
  <section class="card card-front" aria-label="Card front">
    <div class="wordmark">KVRo</div>
    <div class="divider"></div>
    <div class="contact">
      <p class="name">Marcus Hale</p>
      <p class="role">Manager</p>
      <p class="address">Your address, city<br>state, ZIP 0000</p>
      <p class="contact-line">
        <svg viewBox="0 0 12 12" aria-hidden="true"><path d="M2.5 1 L4.5 1 L5.2 3.6 L4 4.6 Q5 7 7.4 8 L8.4 6.8 L11 7.5 L11 9.5 Q10.5 11 9 11 Q1 10 1 3 Q1 1.5 2.5 1 Z" fill="var(--accent)"/></svg>
        555-014-2100
      </p>
      <p class="contact-line">
        <svg viewBox="0 0 12 12" aria-hidden="true"><rect x="1" y="2.5" width="10" height="7" fill="none" stroke="var(--accent)" stroke-width="1.2"/><path d="M1 2.5 L6 6.5 L11 2.5" fill="none" stroke="var(--accent)" stroke-width="1.2"/></svg>
        hello@kvro-av.com
      </p>
      <p class="contact-line">
        <svg viewBox="0 0 12 12" aria-hidden="true"><circle cx="6" cy="6" r="5" fill="var(--accent)"/><path d="M1 6 H11 M6 1 V11 M2.5 3.5 H9.5 M2.5 8.5 H9.5" stroke="var(--card)" stroke-width="0.7"/></svg>
        <span>www.<span class="web-accent">kvro-av</span>.com</span>
      </p>
    </div>
  </section>

  <section class="card card-back" aria-label="Card back">
    <div class="wordmark">KVRo</div>
  </section>
</main>
</body>
</html>
```